Get Up to $ 500,000 in Business Capital within 48 hours

design a flyer offering business capital to businesses. The flyer is going to be mailed to business owners and the flyer needs to immediately capture their attention.
The flyer needs to be bold and professional and really stand-out.
pppppppppppppppppppppppppppppppppppppppppppppppppppppppppppppppppppppppppppppppppppppppppppppppppppppppppppppppppppppppppppppppppppppppppppppppppppppppppppppppppppppppppppppppppppppppppppppppppppppppppppppppppppppppppppppppppppppp

Target Market(s)

business owners

Font styles to use
Serif

Requirements
Must have
• Apply online in minutes at MorvelCapital.com or call 800-TAKE-NOW
Nice to have
• We fund almost every business type. Not a business loan, receive a cash advance on your future sales.

```html
<!DOCTYPE html>
<html lang="en">
<head>
<meta charset="utf-8">
<title>MorvelCapital – Business Capital Flyer</title>
<link rel="stylesheet" href="https://fonts.googleapis.com/css2?family=Montserrat:wght@600;700&family=Carlito:wght@400;700&display=swap">
<style>
  :root {
    --royal: #1b3fd4;
    --royal-deep: #1532c4;
    --sky: #45c7fb;
    --orange: #ff9b00;
    --ink: #000;
    --white: #fff;
    --paper: #f2f2f2;
    --navy-text: #1c3ab0;
  }
  * { margin: 0; padding: 0; box-sizing: border-box; }
  html, body { width: 849px; height: 1200px; overflow: hidden; background: var(--white); }
  .flyer {
    position: relative; width: 849px; height: 1200px; overflow: hidden;
    font-family: "Carlito", "Open Sans", sans-serif;
  }
  .hero-photo {
    position: absolute; left: 0; top: 0; width: 849px; height: 600px;
    background:
      radial-gradient(ellipse 260px 420px at 560px 480px, #1a1a1a 0%, #2b2b2b 60%, rgba(60,60,60,0) 100%),
      linear-gradient(180deg, #c9c9c9 0%, #d8d8d8 45%, #bdbdbd 100%);
  }
  .brand {
    position: absolute; left: 62px; top: 28px;
    font-family: "Montserrat", sans-serif; font-weight: 700; font-size: 33px;
    color: var(--royal); letter-spacing: -0.5px;
  }
  .site-top {
    position: absolute; right: 43px; top: 22px;
    font-weight: 700; font-size: 25px; color: var(--royal);
  }
  .headline {
    position: absolute; left: 62px; top: 118px;
    font-family: "Montserrat", sans-serif; font-weight: 700; font-size: 70px;
    line-height: 73px; color: var(--royal); letter-spacing: -1px;
  }
  .headline-rule {
    position: absolute; left: 62px; top: 349px; width: 84px; height: 10px; background: var(--orange);
  }
  .offer-band {
    position: absolute; left: 0; top: 600px; width: 849px; height: 229px; background: var(--royal);
  }
  .offer-lead, .offer-tail {
    position: absolute; left: 62px; color: var(--white); font-weight: 700; font-size: 28px;
  }
  .offer-lead { top: 26px; }
  .offer-tail { top: 148px; }
  .offer-amount {
    position: absolute; left: 62px; top: 52px;
    font-family: "Montserrat", sans-serif; font-weight: 700; font-size: 90px;
    color: var(--orange); letter-spacing: -2px; line-height: 100px;
  }
  .offer-divider {
    position: absolute; left: 484px; top: 30px; width: 2px; height: 170px; background: var(--white);
  }
  .perk { position: absolute; left: 537px; display: flex; align-items: flex-start; }
  .perk svg { width: 50px; height: 50px; flex: none; }
  .perk-text {
    margin-left: 20px; color: var(--white); font-weight: 700; font-size: 26px; line-height: 31px;
  }
  .perk-credit { top: 26px; }
  .perk-form { top: 116px; }
  .benefit-band {
    position: absolute; left: 0; top: 829px; width: 849px; height: 265px; background: var(--sky);
  }
  .benefit { position: absolute; left: 62px; display: flex; align-items: flex-start; }
  .benefit svg { width: 43px; height: 38px; flex: none; }
  .benefit-text {
    margin-left: 28px; color: var(--white); font-size: 24px; line-height: 32px; width: 620px;
  }
  .benefit-1 { top: 33px; }
  .benefit-2 { top: 127px; }
  .benefit-3 { top: 193px; }
  .benefit-1 svg, .benefit-2 svg, .benefit-3 svg { margin-top: 0; }
  .cta-band {
    position: absolute; left: 0; top: 1094px; width: 849px; height: 106px; background: var(--paper);
  }
  .cta-text {
    position: absolute; left: 62px; top: 12px; font-size: 26px; line-height: 31px; color: var(--navy-text);
  }
  .cta-text strong { font-weight: 700; }
</style>
</head>
<body>
<div class="flyer">
  <div class="hero-photo" role="img" aria-label="Black and white photo of a businessman in a suit seen from behind, looking ahead"></div>
  <div class="brand">MORVELCAPITAL</div>
  <div class="site-top">MorvelCapital.com</div>
  <h1 class="headline">Need<br>business<br>capital?</h1>
  <div class="headline-rule"></div>

  <section class="offer-band">
    <div class="offer-lead">You can qualify for up to</div>
    <div class="offer-amount">500,000</div>
    <div class="offer-tail">in just 24 hours.</div>
    <div class="offer-divider"></div>

    <div class="perk perk-credit">
      <svg viewBox="0 0 50 50" fill="none" stroke="#fff" stroke-width="1.6">
        <rect x="1" y="3" width="44" height="30" rx="2"/>
        <line x1="6" y1="10" x2="16" y2="10"/><rect x="6" y="8" width="10" height="5"/>
        <line x1="6" y1="19" x2="26" y2="19"/><line x1="6" y1="24" x2="22" y2="24"/>
        <circle cx="34" cy="28" r="8" fill="#1b3fd4"/>
        <text x="34" y="32" font-size="11" fill="#fff" stroke="none" text-anchor="middle" font-family="sans-serif" font-weight="700">$</text>
        <line x1="39.5" y1="34" x2="46" y2="44" stroke-width="3"/>
      </svg>
      <div class="perk-text">No minimum<br>credit score</div>
    </div>

    <div class="perk perk-form">
      <svg viewBox="0 0 50 50" fill="none" stroke="#fff" stroke-width="1.6">
        <path d="M2 2 H28 L36 10 V48 H2 Z"/><path d="M28 2 V10 H36"/>
      </svg>
      <div class="perk-text">Simple 1<br>page application</div>
    </div>
  </section>

  <section class="benefit-band">
    <div class="benefit benefit-1">
      <svg viewBox="0 0 43 38"><path d="M11 1 H32 L42 19 L32 37 H11 L1 19 Z" fill="#000"/><path d="M13 19 L19 25 L30 13" stroke="#fff" stroke-width="4" fill="none" stroke-linecap="round" stroke-linejoin="round"/></svg>
      <div class="benefit-text">Not a business loan, get a cash advance today on your future sales.</div>
    </div>
    <div class="benefit benefit-2">
      <svg viewBox="0 0 43 38"><path d="M11 1 H32 L42 19 L32 37 H11 L1 19 Z" fill="#000"/><path d="M13 19 L19 25 L30 13" stroke="#fff" stroke-width="4" fill="none" stroke-linecap="round" stroke-linejoin="round"/></svg>
      <div class="benefit-text">Convenient alternative to a bank loan.</div>
    </div>
    <div class="benefit benefit-3">
      <svg viewBox="0 0 43 38"><path d="M11 1 H32 L42 19 L32 37 H11 L1 19 Z" fill="#000"/><path d="M13 19 L19 25 L30 13" stroke="#fff" stroke-width="4" fill="none" stroke-linecap="round" stroke-linejoin="round"/></svg>
      <div class="benefit-text">We fund virtually every type of business.</div>
    </div>
  </section>

  <footer class="cta-band">
    <p class="cta-text">Apply in minutes online at <strong>MorvelCapital.com</strong> or<br>call <strong>1-800-TAKE-NOW</strong></p>
  </footer>
</div>
</body>
</html>
```